Simple and clean webdesign for personal homepage

Trying to create a simple and clean webdesign for my personal homepage. Going to use a static site builder with templates to build the site. I want it to have multiple pages - like an about me, blog and resume. I just need something very basic I can customize. I want the main colors to be purple, black and white. I am open to other color palettes too but since purple is my favorite color I want that to be one of the main colors.

The site be mostly text driven. Might have some images in the body text but I want the site design to be light and lean.

Industry/Entity Type

Personal Homepage.

Coding

Coded - Design and coding required

Number of Pages Required

1 page

Font styles to use
Sans Serif

Colors
6B429C
8869AF
B7A5CE
E3DAEB
F3F0F8

Requirements
Must have
• Clean design. Purple used as a color. HTML template.
Nice to have
• Responsive

```html
<!DOCTYPE html>
<html lang="en">
<head>
<meta charset="utf-8">
<title>Mara Ellison — Personal Homepage</title>
<link href="https://fonts.googleapis.com/css2?family=Poppins:wght@300;400;500;600&family=Lato:wght@400;700&display=swap" rel="stylesheet">
<style>
:root{
  --purple:#6b3fa0;
  --purple-btn:#6b429c;
  --purple-mid:#8869af;
  --lilac:#b7a5ce;
  --lavender:#e3daeb;
  --mist:#f3f0f8;
  --periwinkle:#6b86e0;
  --ink:#1e1e2a;
  --text:#5b5b66;
  --muted:#9a9aa6;
  --white:#ffffff;
  --footer:#272a46;
  --orange:#f7931e;
}
*{box-sizing:border-box;margin:0;padding:0}
html,body{width:1200px;height:4368px;overflow:hidden}
body{position:relative;background:var(--white);font-family:'Lato',sans-serif;color:var(--text)}
.abs{position:absolute}
.heading{font-family:'Poppins',sans-serif;font-weight:300;color:var(--ink)}
.btn{position:absolute;display:flex;align-items:center;justify-content:space-between;padding:0 24px;font-family:'Lato',sans-serif;font-weight:700;font-size:13px;text-decoration:none}
.btn svg{width:22px;height:12px}
.btn-solid{background:var(--purple-btn);color:var(--white)}
.btn-soft{background:var(--lavender);color:var(--purple-btn)}
.btn-white{background:var(--white);color:var(--purple-btn)}

/* hero */
.hero{position:absolute;left:0;top:0;width:1200px;height:683px;background:var(--purple);overflow:hidden}
.logo{position:absolute;font-family:'Poppins',sans-serif;font-weight:300;font-size:32px;color:var(--white);letter-spacing:.5px}
.nav a{position:absolute;top:34px;font-family:'Poppins',sans-serif;font-size:14px;font-weight:500;color:var(--white);text-decoration:none}
.nav .cta{top:19px;left:912px;width:173px;height:49px;border:1.5px solid rgba(255,255,255,.8);display:flex;align-items:center;justify-content:space-between;padding:0 20px;font-size:14px}
.hero-bar{position:absolute;left:115px;top:237px;width:7px;height:102px;background:var(--white)}
.hero-kicker{position:absolute;left:147px;top:230px;font-family:'Poppins',sans-serif;font-weight:600;font-size:32px;letter-spacing:1.5px;color:var(--white)}
.hero-name{position:absolute;left:143px;top:262px;font-family:'Poppins',sans-serif;font-weight:300;font-size:82px;line-height:1.1;color:var(--white)}
.hero-lead{position:absolute;left:115px;top:378px;width:500px;font-size:19.5px;line-height:32px;font-weight:700;color:var(--white)}
.hero-photo{position:absolute;left:712px;top:93px;width:373px;height:590px;border-radius:180px 180px 0 0;background:linear-gradient(180deg,#2a1a22 0%,#4a2c2a 45%,#2bb3e6 70%,#1ea0dc 100%)}
.side-rail span{position:absolute;left:1141px;transform:rotate(-90deg);transform-origin:left top;font-family:'Poppins',sans-serif;font-size:10px;letter-spacing:2.5px;color:rgba(255,255,255,.55)}
.chat{position:absolute;left:1059px;top:654px;width:58px;height:58px;border-radius:50%;background:var(--orange);box-shadow:0 6px 16px rgba(247,147,30,.45);display:flex;align-items:center;justify-content:center}

/* interests */
.interests-title{left:119px;top:840px;font-size:45px}
.interests-text{left:115px;top:926px;width:380px;font-size:17px;line-height:30px}
.intro-title{left:613px;top:797px;width:470px;font-size:34px;line-height:42px}
.intro-text{left:613px;top:950px;width:470px;font-size:14.5px;line-height:29px}
.stat{position:absolute;top:1060px;display:flex;align-items:center;gap:14px}
.stat b{font-family:'Poppins',sans-serif;font-weight:600;font-size:66px;color:var(--purple-btn);line-height:1}
.stat span{font-size:17px;line-height:22px;color:var(--muted)}

.band{position:absolute;left:0;top:1432px;width:1200px;height:816px;background:var(--mist)}
.service{position:absolute;top:1224px;width:305px;height:318px;background:var(--white);box-shadow:0 10px 30px rgba(60,40,100,.08)}
.service svg{position:absolute;left:28px;top:155px;width:54px;height:54px}
.service h3{position:absolute;left:113px;top:150px;font-family:'Poppins',sans-serif;font-weight:300;font-size:33px;line-height:40px;color:var(--ink)}
.service p{position:absolute;left:113px;top:250px;font-size:13.5px;color:var(--muted)}
.service.active{background:var(--periwinkle)}
.service.active h3,.service.active p{color:var(--white)}

/* about */
.about-photo{left:144px;top:1602px;width:424px;height:646px;border-radius:200px 200px 0 0;background:linear-gradient(180deg,#2a1c18 0%,#5b3b30 40%,#b85c7a 65%,#6e5848 100%)}
.about-title{left:646px;top:1708px;font-size:46px}
.about-lead{left:643px;top:1788px;width:440px;font-size:14.5px;line-height:28px;font-weight:700;color:#4a4a56}
.about-text{left:643px;top:1890px;width:440px;font-size:14.5px;line-height:28px}

/* projects */
.projects-title{left:113px;top:2350px;font-size:46px}
.projects-text{left:114px;top:2434px;width:670px;font-size:14.5px;line-height:28px}
.shot{position:absolute;box-shadow:0 8px 24px rgba(0,0,0,.1)}
.shot-label{position:absolute;font-family:'Poppins',sans-serif;font-weight:500;font-size:25px;color:var(--ink);white-space:nowrap}
.progress{left:273px;top:3114px;width:617px;height:2px;background:var(--lavender)}
.progress i{position:absolute;left:0;top:-1px;width:174px;height:4px;background:var(--periwinkle)}
.arrow-btn{position:absolute;top:3087px;width:48px;height:47px;background:var(--mist);display:flex;align-items:center;justify-content:center}

/* blog */
.blog-band{left:0;top:3233px;width:1200px;height:722px;background:var(--mist)}
.blog-title{left:0;top:3330px;width:1200px;text-align:center;font-size:46px}
.blog-img{position:absolute;top:3437px;width:306px;height:277px}
.blog-date{position:absolute;font-family:'Poppins',sans-serif;font-size:11px;letter-spacing:2px;color:var(--muted)}
.blog-head{position:absolute;width:300px;font-family:'Poppins',sans-serif;font-size:19px;line-height:28px;color:var(--ink)}
.blog-body{position:absolute;width:300px;font-size:13.5px;line-height:26.5px}
.read{position:absolute;top:3840px;font-family:'Poppins',sans-serif;font-weight:600;font-size:12px;letter-spacing:2px;color:var(--purple-btn);border-bottom:1.5px solid var(--purple-btn);padding-bottom:1px}
.blog-nav{position:absolute;top:3587px;color:var(--ink)}

/* footer */
.footer{left:0;top:3955px;width:1200px;height:413px;background:var(--footer);color:#a3a6c0}
.footer .logo{left:111px;top:102px;font-size:36px}
.f-small{position:absolute;font-size:12.5px;line-height:22px;color:#a3a6c0}
.f-head{position:absolute;top:105px;font-family:'Poppins',sans-serif;font-weight:600;font-size:13px;color:var(--white)}
.f-links{position:absolute;top:150px;list-style:none;font-size:12.5px;line-height:30px}
.f-input{position:absolute;left:834px;top:180px;width:251px;height:40px;border:1px solid #4a4e6e;padding:0 16px;display:flex;align-items:center;font-size:12px;font-style:italic;color:#6a6e8c}
.f-sub{position:absolute;left:834px;top:237px;width:251px;height:39px;background:var(--purple-btn);color:var(--white);display:flex;align-items:center;justify-content:center;font-family:'Poppins',sans-serif;font-weight:600;font-size:12px;letter-spacing:1.5px}
.f-dot{position:absolute;top:372px;width:28px;height:28px;border-radius:50%;background:#33375a}
.f-ico{position:absolute;left:113px;width:26px;height:26px;border-radius:50%;background:#33375a;display:flex;align-items:center;justify-content:center}
</style>
</head>
<body>

<!-- Hero -->
<header class="hero">
  <div class="logo" style="left:113px;top:20px">Mara Ellison</div>
  <nav class="nav">
    <a style="left:460px">Home</a>
    <a style="left:546px">About</a>
    <a style="left:639px">Portfolio</a>
    <a style="left:748px">Blog</a>
    <a style="left:829px">Resume</a>
    <a class="cta">Get in touch <svg width="18" height="12" viewBox="0 0 18 12" fill="none" stroke="#fff" stroke-width="1.6"><path d="M0 6h16M11 1l5 5-5 5"/></svg></a>
  </nav>
  <div class="hero-bar"></div>
  <div class="hero-kicker">HELLO, I AM</div>
  <h1 class="hero-name">Mara Ellison</h1>
  <p class="hero-lead">Porin condimentum ornare. Praesent a neque leo. Suspendisse congue, ligula quis tincidunt bibendum sed ammt dictam.</p>
  <a class="btn btn-white" style="left:115px;top:505px;width:173px;height:46px">Meet Mara <svg viewBox="0 0 22 12" fill="none" stroke="currentColor" stroke-width="1.6"><path d="M0 6h20M15 1l5 5-5 5"/></svg></a>
  <div class="hero-photo" role="img" aria-label="Portrait photo of Mara smiling in a blue top"></div>
  <div class="side-rail">
    <span style="top:222px">JOURNAL</span>
    <span style="top:324px">NETWORK</span>
    <span style="top:448px">GALLERY</span>
    <span style="top:552px">UPDATES</span>
  </div>
</header>
<div class="chat"><svg width="26" height="24" viewBox="0 0 26 24" fill="none" stroke="#fff" stroke-width="2"><rect x="2" y="2" width="22" height="15" rx="3"/><path d="M8 17l-2 5 6-5M7 8h12M7 12h8"/></svg></div>

<!-- Interests -->
<h2 class="abs heading interests-title">Area of interests</h2>
<p class="abs interests-text">Porin condimentum ornare. Praesent a neque leo. Suspendisse congue, ligula quis tincidunt bibendum sed.</p>
<a class="btn btn-soft" style="left:115px;top:1046px;width:173px;height:47px">Contact us <svg viewBox="0 0 22 12" fill="none" stroke="currentColor" stroke-width="1.6"><path d="M0 6h20M15 1l5 5-5 5"/></svg></a>

<h2 class="abs heading intro-title">Etiam consectetur pulvinar lorem a laoreet. Nulla ut volutpat lacus</h2>
<p class="abs intro-text">Interdum et malesuada fames ac ante ipsum primis in faucibus. Donec ut suscipit purus. Praesent feugiat, magna sed ultricies ullamcorper, felis quam aliquam orci, ut pulvinar sapien.</p>
<div class="stat" style="left:610px"><b>14</b><span>Years of<br>experience</span></div>
<div class="stat" style="left:848px"><b>187</b><span>Projects<br>completed</span></div>

<div class="band"></div>
<div class="service active" style="left:115px">
  <svg viewBox="0 0 54 54" fill="none" stroke="#fff" stroke-width="2"><path d="M27 6l20 10v22L27 48 7 38V16z"/><path d="M7 16l20 10 20-10M27 26v22M17 11l20 10v8"/></svg>
  <h3>Product<br>Design</h3><p>124 projects</p>
</div>
<div class="service" style="left:447px">
  <svg viewBox="0 0 54 54" fill="none" stroke="#6b86e0" stroke-width="2"><rect x="4" y="8" width="46" height="32" rx="2"/><rect x="9" y="13" width="36" height="22"/><path d="M20 40v6M34 40v6M14 47h26"/><circle cx="27" cy="24" r="5"/></svg>
  <h3>Full Stack<br>Develop</h3><p>37 projects</p>
</div>
<div class="service" style="left:780px">
  <svg viewBox="0 0 54 54" fill="none" stroke="#6b86e0" stroke-width="2"><path d="M27 8l10 18-6 10H23l-6-10z"/><path d="M27 8v14"/><circle cx="27" cy="24" r="2"/><path d="M22 36h10v10H22z"/><circle cx="27" cy="6" r="3"/><path d="M4 14h16M34 14h16"/><circle cx="4" cy="14" r="2.5"/><circle cx="50" cy="14" r="2.5"/></svg>
  <h3>Branding<br>Design</h3><p>62 projects</p>
</div>

<!-- About -->
<div class="abs about-photo" role="img" aria-label="Photo of Mara laughing, arms crossed, in a striped sweater"></div>
<h2 class="abs heading about-title">About me</h2>
<p class="abs about-lead">Interdum et malesuada fames ac ante ipsum primis in faucibus. Donec ut suscipit purus. Praesent feugiat, magna sed ultricies ullamcorper, felis quam aliquam orci, ut pulvinar sapien.</p>
<p class="abs about-text">Sed sollicitudin, enim ut pharetra consequat, nulla metus molestie est, in placerat lorem mi vel elit. In tincidunt, diam vel convallis congue, ante lorem porta odio, consectetur gravida risus lectus nec ipsum. Integer pharetra mauris quis augue rhoncus luctus. Integer semper elit in lacus viverra.</p>
<a class="btn btn-solid" style="left:644px;top:2068px;width:171px;height:46px">Learn more <svg viewBox="0 0 22 12" fill="none" stroke="currentColor" stroke-width="1.6"><path d="M0 6h20M15 1l5 5-5 5"/></svg></a>

<!-- Projects -->
<h2 class="abs heading projects-title">Creative projects</h2>
<a class="btn btn-solid" style="left:915px;top:2365px;width:171px;height:45px">Portfolio <svg viewBox="0 0 22 12" fill="none" stroke="currentColor" stroke-width="1.6"><path d="M0 6h20M15 1l5 5-5 5"/></svg></a>
<p class="abs projects-text">For over 20 years, our Los Angeles web design company has been privileged to offer efficient solutions in website design and development to a diverse clientele. We are always pushing the boundaries and breaking new grounds,and help them succeed.</p>

<div class="shot" style="left:114px;top:2619px;width:315px;height:339px;background:linear-gradient(180deg,#e9ecf2 0%,#c9ccd2 45%,#ffffff 46%,#f4f4f4 100%)" role="img" aria-label="Website screenshot for a kitchen and bath remodeling company"></div>
<div class="shot-label" style="left:116px;top:2980px">Birch Remodeling</div>
<div class="shot" style="left:454px;top:2568px;width:316px;height:339px;background:linear-gradient(180deg,#6e6056 0%,#8a7464 50%,#c7b39d 75%,#efe6dc 100%)" role="img" aria-label="Website screenshot for an insulation contractor"></div>
<div class="shot-label" style="left:455px;top:2924px">Warmline Insulation</div>
<div class="shot" style="left:797px;top:2619px;width:315px;height:347px;background:linear-gradient(180deg,#3b4a3c 0%,#5a6b58 50%,#ffffff 51%,#eef0f2 100%)" role="img" aria-label="Website screenshot for a patio contractor"></div>
<div class="shot-label" style="left:798px;top:2982px">Oakridge Patios</div>
<div class="shot" style="left:1141px;top:2568px;width:80px;height:339px;background:linear-gradient(180deg,#27344f 0%,#3a4c6e 40%,#ffffff 41%,#f2f2f2 100%)" role="img" aria-label="Website screenshot for a roofing company"></div>
<div class="shot-label" style="left:1141px;top:2924px">Kestrel R</div>

<div class="abs progress"><i></i></div>
<div class="arrow-btn" style="left:980px"><svg width="10" height="16" viewBox="0 0 10 16" fill="none" stroke="#c9c4d8" stroke-width="2"><path d="M8 2L2 8l6 6"/></svg></div>
<div class="arrow-btn" style="left:1037px"><svg width="10" height="16" viewBox="0 0 10 16" fill="none" stroke="#6b86e0" stroke-width="2"><path d="M2 2l6 6-6 6"/></svg></div>

<!-- Blog -->
<div class="abs blog-band"></div>
<h2 class="abs heading blog-title">Latet from blog</h2>
<svg class="blog-nav" style="left:74px" width="10" height="16" viewBox="0 0 10 16" fill="none" stroke="#333" stroke-width="1.8"><path d="M8 2L2 8l6 6"/></svg>
<svg class="blog-nav" style="left:1113px" width="10" height="16" viewBox="0 0 10 16" fill="none" stroke="#333" stroke-width="1.8"><path d="M2 2l6 6-6 6"/></svg>

<div class="blog-img" style="left:114px;background:linear-gradient(135deg,#d9dadc 0%,#9a9b9f 55%,#4c4d52 100%)" role="img" aria-label="Photo of hands typing on a laptop"></div>
<div class="blog-date" style="left:114px;top:3736px">29 SEPTEMBER, 2020</div>
<div class="blog-head" style="left:114px;top:3766px">Aliquam cursus tortor neque, a gravida neque gravida</div>
<div class="read" style="left:115px">READ MORE</div>

<div class="blog-date" style="left:446px;top:3439px">29 SEPTEMBER, 2020</div>
<div class="blog-head" style="left:446px;top:3468px">Nam quis quam risus ellent sed esque at mauris eget diam venenatis suscipit...</div>
<p class="blog-body" style="left:446px;top:3562px">Fusce eu enim at nisl dapibus congue. Donec at urna rutrum, luctus velit non, ornare metus. Ut interdum et nisl in tempus. Donec vestibulum odio eu nisl malesuada, nec consequat sem tem por. Aliquam volutpat facilisis efficitur. Ut eget consequat quam, eu posuere augue. Vestibulum rhoncus dui ipsum, sed vulputate magna vehicula nec. Sed ut pulvinar mi. Suspendisse nec nunc sem. In interdum nisl dolor.</p>
<div class="read" style="left:447px">READ MORE</div>

<div class="blog-img" style="left:778px;background:linear-gradient(135deg,#f6c45a 0%,#f2b23e 50%,#d9d9dc 100%)" role="img" aria-label="Photo of a laptop, notebook and coffee on a yellow desk"></div>
<div class="blog-date" style="left:778px;top:3736px">29 SEPTEMBER, 2020</div>
<div class="blog-head" style="left:778px;top:3766px">Aliquam cursus tortor neque, a gravida neque gravida</div>
<div class="read" style="left:779px">READ MORE</div>

<!-- Footer -->
<footer class="abs footer">
  <div class="logo">Mara Ellison</div>
  <p class="f-small" style="left:113px;top:164px">418 Linden Grove Ave, Suite 12,<br>Fairmont, IL 60417</p>
  <div class="f-ico" style="top:219px"><svg width="11" height="8" viewBox="0 0 11 8" fill="#c8cae0"><path d="M0 0h11v8H0z"/><path d="M0 0l5.5 4L11 0" stroke="#33375a" fill="none"/></svg></div>
  <p class="f-small" style="left:151px;top:221px">hello@maraellison.net</p>
  <div class="f-ico" style="top:256px"><svg width="10" height="10" viewBox="0 0 10 10" fill="#c8cae0"><path d="M2 0l2 2.5-1.2 1.3c.6 1.3 1.6 2.3 2.9 2.9L7 5.5 10 8l-1.5 2C4 10 0 6 0 1.5z"/></svg></div>
  <p class="f-small" style="left:151px;top:258px">+044 300 7265</p>

  <div class="f-head" style="left:444px">About</div>
  <ul class="f-links" style="left:444px"><li>Home</li><li>About me</li><li>Portfolio</li><li>Blog</li><li>Resume</li></ul>
  <div class="f-head" style="left:642px">Left</div>
  <ul class="f-links" style="left:642px"><li>Sitemap</li><li>Imprint</li><li>Terms and conditions</li><li>Privacy policy</li></ul>
  <div class="f-head" style="left:832px">Newsletters</div>
  <p class="f-small" style="left:832px;top:144px">Signup below to join our mailing list</p>
  <div class="f-input">Email address</div>
  <div class="f-sub">SUBSCRIBE NOW</div>

  <p class="f-small" style="left:111px;top:375px;font-size:11.5px;color:#c8cae0">© 2021 Maraellison . All rights reserved</p>
  <div class="f-dot" style="left:940px"></div>
  <div class="f-dot" style="left:978px"></div>
  <div class="f-dot" style="left:1017px"></div>
  <div class="f-dot" style="left:1055px"></div>
</footer>

</body>
</html>
```